RTamberly Business Cards & Letterhead

I have a logo but need a design for some new business cards. We are a Design-Build Firm that specializes in the design and construction of commercial projects.
the cards need to be professional. no cartoon stuff.
i would like to have the cards in AI format so I can update the card as needed. Logo is provided.
Our Address is: 4183 Marwood Ln. Apex, North Carolina 27614

```html
<!DOCTYPE html>
<html lang="en">
<head>
<meta charset="utf-8">
<title>RTamberly Business Card</title>
<link href="https://fonts.googleapis.com/css2?family=Montserrat:wght@800&family=Arimo:wght@400;700&display=swap" rel="stylesheet">
<style>
  :root {
    --stage: #2b2b2d;
    --brand-blue: #0a69a6;
    --brand-blue-deep: #064d80;
    --brand-blue-light: #1580c2;
    --paper: #ffffff;
    --paper-shade: #e3e9ef;
    --logo-ink: #2f3236;
    --text-light: #ffffff;
    --text-soft: #d7e6f2;
  }
  html, body {
    margin: 0;
    padding: 0;
    width: 1200px;
    height: 947px;
    overflow: hidden;
    background: var(--stage);
  }
  .canvas {
    position: relative;
    width: 1200px;
    height: 947px;
    background: radial-gradient(ellipse at 50% 45%, #3a3a3d 0%, var(--stage) 70%);
  }
  .card {
    position: absolute;
    width: 560px;
    height: 320px;
    border-radius: 22px;
    overflow: hidden;
    box-shadow: 0 18px 40px rgba(0,0,0,0.55);
  }
  /* Back side */
  .card-back {
    left: 60px;
    top: 90px;
    background: radial-gradient(ellipse at 55% 40%, var(--brand-blue-light) 0%, var(--brand-blue) 45%, var(--brand-blue-deep) 100%);
    display: flex;
    align-items: center;
    justify-content: center;
  }
  .wordmark {
    display: flex;
    align-items: center;
    gap: 10px;
    font-family: "Montserrat", sans-serif;
    font-weight: 800;
    letter-spacing: 1px;
  }
  .wordmark .mark-square {
    width: 26px;
    height: 26px;
    border-radius: 3px;
  }
  .card-back .wordmark {
    font-size: 48px;
    color: var(--text-light);
  }
  .card-back .wordmark .mark-square {
    width: 38px;
    height: 38px;
    background: var(--text-light);
  }
  /* Front side */
  .card-front {
    left: 580px;
    top: 540px;
    background: linear-gradient(90deg, var(--brand-blue-light) 0%, var(--brand-blue) 60%, var(--brand-blue-deep) 100%);
  }
  .front-panel {
    position: absolute;
    left: 0;
    top: 0;
    width: 330px;
    height: 320px;
    background: linear-gradient(160deg, var(--paper) 0%, #f1f4f7 55%, var(--paper-shade) 100%);
    border-radius: 0 60px 140px 0;
    box-shadow: 4px 0 12px rgba(0,0,0,0.25);
  }
  .front-panel .wordmark {
    position: absolute;
    left: 42px;
    top: 140px;
    font-size: 30px;
    color: var(--logo-ink);
  }
  .front-panel .wordmark .mark-square {
    background: var(--brand-blue);
  }
  .contact {
    position: absolute;
    left: 356px;
    top: 50px;
    font-family: "Arimo", sans-serif;
    color: var(--text-light);
  }
  .contact .person-name {
    font-size: 19px;
    font-weight: 700;
    margin: 0;
  }
  .contact .person-title {
    font-size: 12px;
    color: var(--text-soft);
    margin: 2px 0 18px;
  }
  .contact .address {
    font-size: 13px;
    line-height: 17px;
    margin: 0 0 16px;
    font-style: normal;
  }
  .contact ul {
    list-style: none;
    margin: 0;
    padding: 0;
    font-size: 13px;
    line-height: 19px;
  }
  .contact li {
    display: flex;
    align-items: center;
    gap: 8px;
  }
  .contact svg {
    width: 12px;
    height: 12px;
    fill: var(--text-light);
  }
</style>
</head>
<body>
<div class="canvas">
  <section class="card card-back">
    <div class="wordmark"><span class="mark-square"></span>RTAMBERLY</div>
  </section>

  <section class="card card-front">
    <div class="front-panel">
      <div class="wordmark"><span class="mark-square"></span>RTAMBERLY</div>
    </div>
    <div class="contact">
      <p class="person-name">Daniel Morrow</p>
      <p class="person-title">Managing Director</p>
      <address class="address">4183 Marwood Ln. Apex<br>North Carolina 27614</address>
      <ul>
        <li><svg viewBox="0 0 24 24"><path d="M6.6 10.8a15 15 0 0 0 6.6 6.6l2.2-2.2a1 1 0 0 1 1-.25 11.4 11.4 0 0 0 3.6.57 1 1 0 0 1 1 1V20a1 1 0 0 1-1 1A17 17 0 0 1 3 4a1 1 0 0 1 1-1h3.5a1 1 0 0 1 1 1c0 1.25.2 2.45.57 3.6a1 1 0 0 1-.25 1z"/></svg>919-555-0142</li>
        <li><svg viewBox="0 0 24 24"><path d="M7 1h10a2 2 0 0 1 2 2v18a2 2 0 0 1-2 2H7a2 2 0 0 1-2-2V3a2 2 0 0 1 2-2zm0 3v14h10V4z"/></svg>919-555-0187</li>
        <li><svg viewBox="0 0 24 24"><path d="M2 5h20v14H2zm2 2v.5l8 5 8-5V7zm0 2.8V17h16V9.8l-8 5z"/></svg>info@rtamberly.com</li>
        <li><svg viewBox="0 0 24 24"><circle cx="12" cy="12" r="10"/></svg>www.rtamberly.com</li>
      </ul>
    </div>
  </section>
</div>
</body>
</html>
```